Creative/innovative law firm website

A law firm website that immediately looks different from other law firm websites. We like the color scheme (dark background with warm, neutral colors) and simple, organic logos (trees, leaves, etc.) of this website: https://brambleworth.legal/

We'll be offering creative/innovative solutions to complex problems faced by state governments, industries, other law firms, and individuals. We're located in Montana (U.S.A.), and the outdoors is a huge part of our lives and identities.

We will need a home page, an "About Us" page with a separate subpage for each attorney (two attorneys), a blog or "Publications" page, a payment portal (which will integrate with Quillo), and a "Services" page.

```html
<!DOCTYPE html>
<html lang="en">
<head>
<meta charset="utf-8">
<title>Ashgrove &amp; Tamsin P.C.</title>
<link href="https://fonts.googleapis.com/css2?family=DM+Serif+Display&family=Montserrat:wght@400;500;600;700&display=swap" rel="stylesheet">
<style>
:root{
  --ink:#0b0f22;
  --navy:#121833;
  --navy-2:#1a2146;
  --panel:#1d2448;
  --gold:#c9934c;
  --gold-soft:#e0b27a;
  --text:#f1ece4;
  --muted:#a9adbf;
  --line:#2c3460;
}
*{box-sizing:border-box;margin:0;padding:0}
html,body{width:1200px;height:4000px;overflow:hidden}
body{background:var(--ink);color:var(--text);font-family:"Montserrat",sans-serif;font-size:14px;line-height:1.6;position:relative}
.serif{font-family:"DM Serif Display",serif;font-weight:400}
.abs{position:absolute}
.btn{display:inline-flex;align-items:center;gap:10px;background:var(--gold);color:#fff;font-size:12px;font-weight:600;letter-spacing:.06em;text-transform:uppercase;padding:10px 18px}
.btn .dot{width:18px;height:18px;border-radius:50%;background:#fff;display:inline-block;position:relative}
.btn .dot::after{content:"";position:absolute;left:6px;top:5px;border-left:7px solid var(--gold);border-top:4px solid transparent;border-bottom:4px solid transparent}
.photo{position:absolute}

/* top */
.topbar{top:0;left:0;width:1200px;height:40px;background:#070a18;display:flex;align-items:center;padding:0 150px;font-size:12px;color:var(--muted);gap:24px}
.topbar .right{margin-left:auto;display:flex;gap:28px}
.ico{display:inline-block;width:10px;height:10px;border-radius:50%;background:var(--gold);margin-right:8px;vertical-align:-1px}
.nav{top:40px;left:0;width:1200px;height:64px;display:flex;align-items:center;padding:0 150px;z-index:2}
.brand{display:flex;align-items:center;gap:10px;font-family:"DM Serif Display",serif;font-size:20px;color:var(--text)}
.brand .mark{width:22px;height:22px;border-radius:50%;background:var(--gold)}
.menu{margin-left:auto;display:flex;gap:26px;font-size:12px;font-weight:600;letter-spacing:.05em}
.menu a{color:var(--text);text-decoration:none}
.menu a.active{color:var(--gold)}
.nav .btn{margin-left:30px;padding:7px 14px}

/* hero */
.hero{top:0;left:0;width:1200px;height:600px;background:linear-gradient(180deg,rgba(11,15,34,.55),rgba(11,15,34,.85)),linear-gradient(110deg,#5a5654,#8c7d6d 45%,#a08a70 55%,#4a4748)}
.hero-copy{top:260px;left:0;width:1200px;text-align:center}
.hero-copy h1{font-size:56px;line-height:1.05}
.hero-copy p{width:340px;margin:18px auto 26px;font-size:13px;color:#ddd}
.social{top:548px;left:548px;display:flex;gap:14px}
.social span{width:28px;height:28px;border-radius:50%;border:1px solid var(--text);display:block}

/* features */
.features{top:600px;left:150px;width:900px;height:120px;display:flex}
.feature{flex:1;display:flex;gap:16px;padding:28px 24px;background:var(--navy)}
.feature.highlight{background:var(--gold)}
.feature .icon{width:42px;height:42px;border:2px solid var(--gold);border-radius:8px;flex:none}
.feature.highlight .icon{border-color:#fff}
.feature h3{font-size:20px;line-height:1.1;margin-bottom:6px}
.feature p{font-size:11px;color:var(--muted);line-height:1.5}
.feature.highlight p{color:#fff}

/* about */
.about-copy{top:790px;left:150px;width:430px}
h2.title{font-size:46px;line-height:1.1;margin-bottom:20px}
.body{font-size:13px;color:var(--muted)}
.about-copy .btn{margin-top:26px}
.about-frame{top:830px;left:614px;width:410px;height:330px;border:3px solid var(--gold)}
.badge-exp{top:1118px;left:826px;background:var(--gold);padding:14px 20px;font-family:"DM Serif Display",serif;font-size:22px}

/* offering */
.offer{top:1230px;left:0;width:1200px;height:700px;background:linear-gradient(180deg,#0f1430,#141b3c)}
.offer-head{top:1290px;left:150px;width:440px}
.offer-text{top:1300px;left:620px;width:420px}
.cards{top:1466px;left:160px;display:flex;gap:28px}
.card{width:270px;height:410px;background:var(--navy-2);border:3px solid var(--gold);padding:12px;text-align:center}
.card .photo{position:relative;height:180px}
.card h3{font-size:22px;line-height:1.15;margin:22px 0 12px}
.card p{font-size:12px;color:var(--muted);padding:0 10px}
.card .arrow{margin-top:20px}

/* testimonial */
.testi-head{top:1980px;left:0;width:1200px;text-align:center}
.testi-head h2{font-size:42px}
.testi-head p{width:360px;margin:6px auto 0;font-size:12px;color:var(--muted)}
.quote{top:2120px;width:440px;height:240px;background:#fff;color:#333;padding:26px 28px}
.quote .who{display:flex;gap:16px;align-items:center;margin-bottom:18px}
.quote .avatar{width:64px;height:64px;border-radius:50%;background:linear-gradient(135deg,#b59b85,#6c5e58)}
.quote h4{font-size:18px;color:var(--ink)}
.quote small{font-size:11px;color:#888}
.quote p{font-size:12px;color:#666}
.quote .qm{position:absolute;right:26px;top:16px;font-family:"DM Serif Display",serif;font-size:60px;color:var(--gold);line-height:1}
.slide-arrow{top:2230px}

/* articles */
.art-copy{top:2470px;left:150px;width:420px}
.post-meta{font-size:10px;color:var(--gold);letter-spacing:.05em}
.post h3{font-size:20px;line-height:1.15;margin-top:4px}

/* achievement */
.ach{top:3020px;left:0;width:1200px;height:520px;background:linear-gradient(180deg,#141b3c,#0d1229)}
.ach-head{top:3100px;left:0;width:1200px;text-align:center}
.ach-head h2{font-size:46px}
.ach-head p{width:330px;margin:8px auto 0;font-size:12px;color:var(--muted)}
.awards{top:3290px;left:190px;display:flex;gap:95px}
.award{width:150px;text-align:center}
.award .seal{width:70px;height:70px;margin:0 auto 14px;border-radius:50%;background:linear-gradient(135deg,var(--gold-soft),#8c5d2a)}
.award h4{font-size:16px}

/* footer */
.footer{top:3540px;left:0;width:1200px;height:460px;background:#0a0e1f}
.foot-brand{top:3600px;left:150px;width:380px}
.foot-brand .brand{font-size:22px;margin-bottom:14px}
.contact-line{font-size:12px;color:var(--muted);margin-top:14px}
.form{top:3600px;left:616px;width:428px}
.form h4{font-size:20px;margin-bottom:14px}
.field{background:var(--panel);height:36px;font-size:11px;color:var(--muted);padding:10px 12px}
.grid{display:grid;grid-template-columns:1fr 1fr;gap:10px;margin-bottom:10px}
.field.tall{height:84px}
.form .btn{margin-top:14px}
.foot-bottom{top:3930px;left:150px;width:900px;display:flex;align-items:center;border-top:1px solid var(--line);padding-top:22px;font-size:11px;color:var(--muted)}
.foot-bottom .links{margin-left:auto;display:flex;gap:22px;font-weight:600;color:var(--text)}
.foot-bottom .social{position:static;display:flex;gap:10px}
.foot-bottom .social span{width:24px;height:24px}
.foot-bottom .copy{margin-left:40px}
</style>
</head>
<body>

<section class="hero abs" role="img" aria-label="Photograph of hands shaking before a courthouse balance scale with a city skyline at dusk"></section>
<div class="topbar abs"><span><i class="ico"></i>Located in Montana (U.S.A)</span><div class="right"><span><i class="ico"></i>hello@ashgrovetamsin.law</span><span><i class="ico"></i>(406) 555-0142</span></div></div>
<header class="nav abs">
  <div class="brand"><span class="mark"></span>Ashgrove &amp; Tamsin P.C.</div>
  <nav class="menu"><a class="active" href="#">HOME</a><a href="#">ABOUT US</a><a href="#">SERVICES</a><a href="#">PUBLICATIONS</a></nav>
  <span class="btn">(406) 555-0142</span>
</header>
<div class="hero-copy abs">
  <h1 class="serif">Simple solution to<br>complex question</h1>
  <p>Clear counsel for hard problems. We listen first, then build practical answers that fit the way you live and work.</p>
  <span class="btn">Begin Consultation <span class="dot"></span></span>
</div>
<div class="social abs"><span></span><span></span><span></span></div>

<section class="features abs">
  <div class="feature"><span class="icon"></span><div><h3 class="serif">Experienced</h3><p>Decades of trial and advisory work across the state.</p></div></div>
  <div class="feature highlight"><span class="icon"></span><div><h3 class="serif">Effective</h3><p>Focused strategy that moves matters forward.</p></div></div>
  <div class="feature"><span class="icon"></span><div><h3 class="serif">Here For You</h3><p>Direct access to your attorney at every step.</p></div></div>
</section>

<section class="about-copy abs">
  <h2 class="title serif">About Ashgrove &amp;<br>Tamsin P.C.</h2>
  <p class="body">We are a Montana firm built on the belief that law can be creative without being careless. Our attorneys combine deep experience with fresh thinking to solve problems others call impossible. We work closely with each client, keep our advice plain, and stay with every matter until it is done right.</p>
  <p class="body" style="margin-top:12px">From public agencies to private companies, we bring the same care, candor and steady judgment to every case we accept.</p>
  <span class="btn">More About Us <span class="dot"></span></span>
</section>
<div class="about-frame abs"></div>
<div class="photo" style="top:850px;left:638px;width:410px;height:300px;background:linear-gradient(135deg,#e9e6e2,#9aa0ab 60%,#3c3f4a)" role="img" aria-label="Photograph of two attorneys reviewing documents at a desk"></div>
<div class="badge-exp abs">15 Years Experience</div>

<section class="offer abs"></section>
<div class="offer-head abs">
  <h2 class="title serif">We are offering creative<br>innovative solutions</h2>
  <span class="btn">View All Services <span class="dot"></span></span>
</div>
<p class="offer-text abs body">Every client faces a different set of pressures. We study the full picture, weigh the risks, and design answers that hold up in practice. Our approach blends careful research with practical experience so that solutions are sound, timely and easy to act on.</p>
<div class="cards abs">
  <article class="card"><div class="photo" style="background:linear-gradient(180deg,#5d87c4,#dfe6ee 60%,#4f7a3a)" role="img" aria-label="Photograph of a white government building with a lawn"></div><h3 class="serif">Problems From<br>State Governments</h3><p>Guidance on policy, compliance and public law questions.</p><svg class="arrow" width="34" height="14"><path d="M2 7h28M24 2l6 5-6 5" stroke="#c9934c" stroke-width="2" fill="none"/></svg></article>
  <article class="card"><div class="photo" style="background:linear-gradient(135deg,#2b2a2c,#7a6a5c 60%,#2a2426)" role="img" aria-label="Photograph of a professional in a suit signing a document"></div><h3 class="serif">Problems From<br>Industries</h3><p>Regulatory, contract and dispute help for growing businesses.</p><svg class="arrow" width="34" height="14"><path d="M2 7h28M24 2l6 5-6 5" stroke="#c9934c" stroke-width="2" fill="none"/></svg></article>
  <article class="card"><div class="photo" style="background:linear-gradient(135deg,#5b3a26,#a67b52 55%,#2c1d16)" role="img" aria-label="Photograph of a lawyer standing in a library of law books"></div><h3 class="serif">Problems From<br>Other Law Firms</h3><p>Co-counsel and strategic support on complex matters.</p><svg class="arrow" width="34" height="14"><path d="M2 7h28M24 2l6 5-6 5" stroke="#c9934c" stroke-width="2" fill="none"/></svg></article>
</div>

<div class="testi-head abs"><h2 class="serif">Testimonial</h2><p>Words from clients who trusted us with their most demanding legal challenges.</p></div>
<svg class="slide-arrow abs" style="left:100px" width="20" height="20"><path d="M16 10H4M9 4l-6 6 6 6" stroke="#f1ece4" stroke-width="2" fill="none"/></svg>
<svg class="slide-arrow abs" style="left:1080px" width="20" height="20"><path d="M4 10h12M11 4l6 6-6 6" stroke="#f1ece4" stroke-width="2" fill="none"/></svg>
<div class="quote abs" style="left:150px"><span class="qm">”</span><div class="who"><div class="avatar" role="img" aria-label="Client portrait"></div><div><h4 class="serif">Nolan Whitcombe</h4><small>Manager</small></div></div><p>The team took a problem we had struggled with for years and gave us a clear plan in weeks. Calm, honest and always available when we needed them most.</p></div>
<div class="quote abs" style="left:610px"><span class="qm">”</span><div class="who"><div class="avatar" role="img" aria-label="Client portrait"></div><div><h4 class="serif">Reid Castellan</h4><small>Manager</small></div></div><p>Sharp thinking and plain talk. They explained every option, stood by our side in the hard moments, and delivered a result that exceeded our hopes.</p></div>

<section class="art-copy abs">
  <h2 class="title serif" style="margin-bottom:12px">View Our Latest Article</h2>
  <p class="body" style="margin-bottom:22px">Notes and analysis from our attorneys on new rulings, policy shifts and practical steps for clients.</p>
  <span class="btn">View All Articles <span class="dot"></span></span>
</section>
<div class="photo" style="top:2690px;left:158px;width:204px;height:214px;background:linear-gradient(135deg,#d9cfc2,#8c7a6a 60%,#3e3a3c)" role="img" aria-label="Photograph of an older couple meeting with an advisor"></div>
<div class="photo" style="top:2690px;left:372px;width:204px;height:214px;background:linear-gradient(135deg,#5a4a3c,#a58d72 55%,#2b2624)" role="img" aria-label="Photograph of two professionals talking at a table"></div>
<div class="photo" style="top:2490px;left:686px;width:354px;height:400px;background:linear-gradient(135deg,#d8d6d3,#8b8178 55%,#3b3533)" role="img" aria-label="Photograph of a lawyer in glasses reading papers"></div>
<div class="post abs" style="top:2912px;left:158px;width:204px"><div class="post-meta">APRIL 8, 2021</div><h3 class="serif" style="font-size:15px">Prevent A Further Breach of The Peace In The States</h3></div>
<div class="post abs" style="top:2912px;left:372px;width:204px"><div class="post-meta">APRIL 8, 2021</div><h3 class="serif" style="font-size:15px">Prevent A Further Breach of The Peace In The States</h3></div>
<div class="post abs" style="top:2900px;left:686px;width:354px"><div class="post-meta">APRIL 8, 2021</div><h3 class="serif">An Independent Examination Of Charity Accounts</h3></div>

<section class="ach abs"></section>
<div class="ach-head abs"><h2 class="serif">Our Achievement</h2><p>Recognition earned through years of steady, careful work for our clients.</p></div>
<div class="awards abs">
  <div class="award"><div class="seal"></div><h4 class="serif">Best Law Firm 2020</h4></div>
  <div class="award"><div class="seal"></div><h4 class="serif">Best Law Firm 2020</h4></div>
  <div class="award"><div class="seal"></div><h4 class="serif">Best Law Firm 2020</h4></div>
  <div class="award"><div class="seal"></div><h4 class="serif">Best Law Firm 2020</h4></div>
</div>

<footer class="footer abs"></footer>
<div class="foot-brand abs">
  <div class="brand"><span class="mark"></span>Ashgrove &amp; Tamsin P.C.</div>
  <p class="body" style="font-size:12px">Practical counsel rooted in Montana. We help public and private clients find clear paths through complex legal ground.</p>
  <p class="contact-line"><i class="ico"></i>Located in Montana (U.S.A)</p>
  <p class="contact-line"><i class="ico"></i>hello@ashgrovetamsin.law</p>
  <p class="contact-line"><i class="ico"></i>(406) 555-0142</p>
</div>
<div class="form abs">
  <h4 class="serif">Quick Contact</h4>
  <div class="grid"><div class="field">Name</div><div class="field">Email Address</div><div class="field">Phone</div><div class="field">Subject</div></div>
  <div class="field tall">Leave your message</div>
  <span class="btn">Submit Now <span class="dot"></span></span>
</div>
<div class="foot-bottom abs">
  <div class="social"><span></span><span></span><span></span></div>
  <div class="links"><span>HOME</span><span>ABOUT US</span><span>SERVICES</span><span>PUBLICATIONS</span></div>
  <span class="copy">© 2021 Ashgrove &amp; Tamsin P.C.</span>
</div>

</body>
</html>
```